International Medical Company Needs a Website Design for a Support Site

We need a website design for a support site we are doing for ostomates called Bright Rebounds. We are an international company but this website is for our Australian market.

The website is a support site for people who are living with an Ostomy or Bowel Disease. This is a site where they can read other ostomates' stories and how they are dealing with the fact that they have to wear a pouch everyday.

The URL for our US site is: http://www.brightrebounds-example.com/

We need to use the same logo but we have freedom around the color scheme. We are not fond of the brown color scheme used in our US site and are happy for designs to be submitted with alternatives.

• We want the design to be clean, inspiring, modern and inviting.
• We would like to see a design for the mainpage / homepage and one of the subpages
• We only require the PSD / image files (no HTML needed)

Attached to this project is our sitemap, an example wireframe and the logos. We are happy for you to play around with different options and don't have to stick to the layout shown in the wireframe.

If you have any further questions please ask.

```html
<!DOCTYPE html>
<html lang="en">
<head>
<meta charset="utf-8">
<title>Bright Rebounds – Sharing Stories and Giving Hope</title>
<link rel="stylesheet" href="https://fonts.googleapis.com/css2?family=Mulish:wght@300;400;600;700&family=Cabin:wght@400;500;600&display=swap">
<style>
:root{
  --teal:#3fb7d2;
  --teal-light:#6fd0e3;
  --teal-dark:#1e8aa3;
  --gold:#e0a10f;
  --ink:#333;
  --muted:#555;
  --footer:#2b2b2b;
  --white:#fff;
}
*{box-sizing:border-box;margin:0;padding:0}
html,body{width:1200px;height:1054px;overflow:hidden;background:var(--white)}
body{position:relative;font-family:"Mulish",sans-serif;color:var(--ink)}
.site-header{position:absolute;left:0;top:0;width:1200px;height:117px;background:var(--white);border-bottom:1px solid #dfe7ea}
.brand{position:absolute;left:121px;top:58px;display:flex;align-items:center;gap:8px;font:700 14px "Mulish",sans-serif;letter-spacing:1px;color:#222;text-transform:uppercase}
.brand-dot{width:22px;height:22px;border-radius:50%;background:#222}
.utility{position:absolute;left:740px;top:28px;font-size:13px;color:#555;display:flex;gap:14px;align-items:center}
.utility .sep{color:#888}
.search{position:absolute;left:921px;top:18px;width:155px;height:34px;border:1px solid #d5d5d5;background:#f7f7f7;font-size:12px;color:#999;padding:9px 10px}
.search svg{position:absolute;right:9px;top:8px}
.main-nav{position:absolute;left:434px;top:71px;display:flex;font-size:13px;color:#333}
.main-nav a{padding:8px 12px;text-decoration:none;color:inherit;border:2px solid transparent;border-radius:2px}
.main-nav a.active{border-color:var(--teal)}
.hero{position:absolute;left:0;top:117px;width:1200px;height:335px;background:linear-gradient(120deg,var(--teal-light),var(--teal) 55%,#2ea9c7);overflow:hidden}
.hero::before{content:"";position:absolute;left:-80px;top:-40px;width:500px;height:480px;background:rgba(255,255,255,.08);transform:rotate(35deg)}
.hero-title{position:absolute;left:120px;top:70px;font:600 20px "Cabin",sans-serif;color:var(--white);text-shadow:0 1px 2px rgba(0,0,0,.25)}
.hero-text{position:absolute;left:120px;top:103px;width:350px;font:400 16px/19px "Cabin",sans-serif;color:var(--white);text-shadow:0 1px 2px rgba(0,0,0,.25)}
.hero-actions{position:absolute;left:120px;top:200px;display:flex;align-items:center;gap:12px}
.btn-dark{display:inline-block;padding:10px 12px;background:#1c1c1c;border:2px solid #9aa;color:var(--white);font:500 14px "Cabin",sans-serif;box-shadow:0 2px 3px rgba(0,0,0,.3)}
.hero-or{font:italic 13px "Cabin",sans-serif;color:var(--white)}
.slider{position:absolute;left:496px;top:34px;width:580px;height:270px;border:2px solid var(--gold);background:linear-gradient(180deg,#16375d 0%,#2f5f8a 45%,#6a6f7a 75%,#8c6e5c 100%)}
.slider-caption{position:absolute;left:64px;top:188px;font:600 18px "Cabin",sans-serif;color:var(--white);text-shadow:0 1px 3px rgba(0,0,0,.6)}
.slider-arrow{position:absolute;top:110px;width:28px;height:48px;background:var(--gold)}
.slider-arrow.prev{left:-2px;border-radius:0 24px 24px 0}
.slider-arrow.next{right:-2px;border-radius:24px 0 0 24px}
.slider-arrow svg{position:absolute;top:16px}
.feature{position:absolute;top:502px;width:300px}
.feature h2{font:400 20px "Mulish",sans-serif;color:#444;margin-bottom:13px}
.feature h2 strong{color:var(--gold);font-weight:600}
.feature-media{width:300px;height:178px}
.feature p{margin-top:20px;font:300 13px/19.5px "Mulish",sans-serif;color:var(--muted)}
.btn-read{position:absolute;top:337px;left:0;width:94px;height:35px;background:linear-gradient(#2aa3bc,var(--teal-dark));color:var(--white);font:600 13px/35px "Mulish",sans-serif;text-align:center;text-shadow:0 1px 1px rgba(0,0,0,.3)}
.site-footer{position:absolute;left:0;top:938px;width:1200px;height:116px;background:var(--footer);border-top:3px solid #bbb}
.footer-links{position:absolute;left:122px;top:26px;font-size:13px;color:#ddd;display:flex;gap:11px}
.copyright{position:absolute;left:122px;top:50px;font-size:13px;color:#ddd}
.social{position:absolute;left:882px;top:37px;display:flex;gap:11px}
.social span{width:26px;height:26px;border-radius:50%;background:var(--gold)}
</style>
</head>
<body>
<header class="site-header">
  <div class="brand"><span class="brand-dot"></span>Bright Rebounds</div>
  <div class="utility"><span>Share a Story</span><span class="sep">|</span><span>Country ⌄</span></div>
  <div class="search">Search
    <svg width="16" height="16" viewBox="0 0 16 16"><circle cx="10" cy="6" r="4.5" fill="none" stroke="#3fb7d2" stroke-width="2"/><line x1="7" y1="9" x2="2" y2="14" stroke="#3fb7d2" stroke-width="2.5"/></svg>
  </div>
  <nav class="main-nav">
    <a class="active">HOME</a><a>ABOUT US</a><a>PERSONAL STORIES</a><a>TIPS FOR LIVING</a><a>NEWS</a><a>RESOURCES</a><a>CONTACT US</a>
  </nav>
</header>

<section class="hero">
  <h1 class="hero-title">SHARING STORIES AND GIVING HOPE</h1>
  <p class="hero-text">to people around the world who are facing inflammatory bowel disease, colorectal cancer, or have had ostomy surgery.</p>
  <div class="hero-actions"><span class="btn-dark">SHARE A STORY</span><span class="hero-or">or</span><span class="btn-dark">READ STORIES</span></div>
  <div class="slider" role="img" aria-label="Sprinter crouched in starting blocks on a stadium track at dusk">
    <div class="slider-arrow prev"><svg x="0" width="20" height="16" viewBox="0 0 20 16" style="left:6px"><polyline points="12,1 6,8 12,15" fill="none" stroke="#fff" stroke-width="2"/></svg></div>
    <div class="slider-caption">START A NEW JOURNEY TO YOUR LIFE...</div>
    <div class="slider-arrow next"><svg width="20" height="16" viewBox="0 0 20 16" style="left:4px"><polyline points="8,1 14,8 8,15" fill="none" stroke="#fff" stroke-width="2"/></svg></div>
  </div>
</section>

<section class="feature" style="left:121px">
  <h2><strong>What is</strong> Bright Rebounds</h2>
  <div class="feature-media" role="img" aria-label="Swimmer splashing through water against a dark background" style="background:radial-gradient(ellipse at 55% 75%,#5fd0f0,#1a3c8a 45%,#050510 75%)"></div>
  <p>Bright Rebounds® Recognizes Former Principal, Daniel Marlow, As National Award Recipient Lifelong educator pays it forward by teaching others how to succeed after ostomy surgery...</p>
  <span class="btn-read">Read More</span>
</section>

<section class="feature" style="left:448px">
  <h2><strong>Share</strong> a Story</h2>
  <div class="feature-media" role="img" aria-label="Hands typing on a laptop keyboard" style="background:linear-gradient(135deg,#f5b830,#f08a20 45%,#c9c9c4 60%,#e9edd8)"></div>
  <p>Bright Rebounds® Recognizes Former Principal, Daniel Marlow, As National Award Recipient Lifelong educator pays it forward by teaching others how to succeed after ostomy surgery...</p>
  <span class="btn-read">Read More</span>
</section>

<section class="feature" style="left:774px">
  <h2><strong>News</strong> Updates</h2>
  <div class="feature-media" role="img" aria-label="Surgical team in blue scrubs under operating lights" style="background:linear-gradient(160deg,#4a7fc6,#2b5aa8 50%,#1d3f7a)"></div>
  <p>Bright Rebounds® Recognizes Former Principal, Daniel Marlow, As National Award Recipient Lifelong educator pays it forward by teaching others how to succeed after ostomy surgery...</p>
  <span class="btn-read">Read More</span>
</section>

<footer class="site-footer">
  <div class="footer-links"><span>Legal Notice</span><span>|</span><span>Privacy Policy</span><span>|</span><span>Sitemap</span></div>
  <div class="copyright">Copyright@2014, Bright Rebounds</div>
  <div class="social" aria-label="Social links"><span aria-label="Social link one"></span><span aria-label="Social link two"></span><span aria-label="Social link three"></span></div>
</footer>
</body>
</html>
```